Event flyer for Sunday night Youth Group

Need a 4 x 6 or 5 x 7 flyer for a new youth group starting on April 14. The youth group is for students in middle school and high school so it needs to look fun and cool, but not childish. I prefer it not to include pictures of people unless it's so obscure you can't really see their faces. I've uploaded some pictures of flyers I like. I've also attached a couple versions of our logo to use on the flyer.
Information the flyer needs to include:
Youth Group
Sundays, 6-8pm (beginning April 14)
Location: Merriwick's - 4219 Hollowfern Ln S, Ashbrook, 97418
There will be dinner, games, friends, and a message.
Target Market(s)
Youth ages 13-18
Industry/Entity Type
Church
Colors
Designer to choose colors to be used in the design.
Look and feel

```html
<!DOCTYPE html>
<html lang="en">
<head>
<meta charset="utf-8">
<title>Youth Group – Brightway Fellowship</title>
<link rel="stylesheet" href="https://fonts.googleapis.com/css2?family=Allura&family=Anton&family=Outfit:wght@400;600;700&display=swap">
<style>
  :root {
    --page-bg: #0a7fbf;
    --deep-blue: #2b2f92;
    --sky: #3aa6d4;
    --violet: #6a34a8;
    --plum: #2a0f4e;
    --ink-circle: #23246e;
    --white: #ffffff;
    --yellow: #f6ec2a;
    --yellow-light: #fff585;
    --yellow-dark: #c9b60c;
  }
  * { box-sizing: border-box; margin: 0; padding: 0; }
  html, body { width: 1200px; height: 872px; overflow: hidden; }
  body { background: var(--page-bg); position: relative; font-family: "Outfit", sans-serif; }

  .flyer {
    position: absolute; left: 300px; top: 16px;
    width: 600px; height: 840px; overflow: hidden;
    color: var(--white); text-align: center;
  }
  .flyer__backdrop {
    position: absolute; inset: 0;
    background:
      radial-gradient(ellipse 70% 18% at 35% 42%, rgba(110,200,235,.75), transparent 70%),
      radial-gradient(ellipse 60% 14% at 70% 18%, rgba(90,170,225,.6), transparent 70%),
      radial-gradient(ellipse 80% 16% at 60% 66%, rgba(150,140,220,.55), transparent 70%),
      linear-gradient(180deg, var(--deep-blue) 0%, #2f63b8 22%, var(--sky) 42%, #5a73c4 60%, var(--violet) 78%, var(--plum) 100%);
  }
  .flyer__frame {
    position: absolute; inset: 12px;
    border: 1.5px solid var(--white);
  }
  .brand { position: absolute; left: 0; right: 0; top: 38px; }
  .brand__mark {
    width: 58px; height: 58px; margin: 0 auto 24px;
    background: var(--white);
  }
  .brand__name {
    font-weight: 600; font-size: 25px; letter-spacing: 1px; line-height: 1.15;
  }
  .brand__name span { display: block; font-weight: 400; font-size: 14px; letter-spacing: 6px; }

  .ink-circle {
    position: absolute; left: 90px; top: 200px;
    width: 422px; height: 422px; border-radius: 50%;
    background: radial-gradient(circle at 50% 45%, #2b2d85 0%, var(--ink-circle) 70%, rgba(35,36,110,.85) 100%);
  }

  .title-script {
    position: absolute; left: 0; right: 0; top: 212px;
    font-family: "Allura", cursive; font-size: 190px; line-height: 1;
    color: var(--white); text-shadow: 2px 3px 4px rgba(0,0,0,.35);
    z-index: 2;
  }
  .title-block {
    position: absolute; left: 0; right: 0; top: 338px;
    font-family: "Anton", sans-serif; font-size: 150px; line-height: 1;
    letter-spacing: 1px;
    background: linear-gradient(180deg, var(--yellow-light) 0%, var(--yellow) 38%, var(--yellow-dark) 52%, #b8a708 100%);
    -webkit-background-clip: text; background-clip: text; color: transparent;
    z-index: 1;
  }
  .schedule {
    position: absolute; left: 0; right: 0; top: 505px;
    font-weight: 600; font-size: 30px; line-height: 1;
  }
  .start-date {
    position: absolute; left: 0; right: 0; top: 541px;
    font-weight: 600; font-size: 24px; line-height: 1.17; color: var(--yellow);
  }

  .offerings {
    position: absolute; left: 110px; top: 657px; width: 381px; height: 88px;
    border: 2px solid var(--yellow); border-top: none;
  }
  .offerings::before, .offerings::after {
    content: ""; position: absolute; top: 0; height: 2px; width: 46px; background: var(--yellow);
  }
  .offerings::before { left: 0; }
  .offerings::after { right: 0; }
  .offerings__title {
    position: absolute; left: 0; right: 0; top: -18px;
    font-weight: 600; font-size: 33px; line-height: 1;
  }
  .offerings__list {
    position: absolute; left: 0; right: 0; top: 20px;
    font-weight: 600; font-size: 23px; line-height: 1.38;
  }
  .offerings__list .highlight { color: var(--yellow); display: block; }

  .venue {
    position: absolute; left: 138px; top: 760px; width: 362px;
    font-weight: 600; font-size: 18px; line-height: 1.4; color: var(--yellow);
    text-align: center;
  }
  .venue__pin { position: absolute; left: 106px; top: 762px; width: 24px; height: 32px; }
</style>
</head>
<body>
  <article class="flyer">
    <div class="flyer__backdrop" role="img" aria-label="Blue and purple watercolour wash background"></div>
    <div class="flyer__frame"></div>

    <header class="brand">
      <div class="brand__mark"></div>
      <p class="brand__name">BRIGHTWAY<span>FELLOWSHIP</span></p>
    </header>

    <div class="ink-circle" role="img" aria-label="Dark navy brush-painted circle"></div>

    <h1>
      <span class="title-script">Youth</span>
      <span class="title-block">GROUP</span>
    </h1>

    <p class="schedule">SUNDAYS, 6–8PM</p>
    <p class="start-date">BEGINNING<br>APRIL 14</p>

    <section class="offerings">
      <h2 class="offerings__title">THERE WILL BE</h2>
      <p class="offerings__list">
        <span class="highlight">DINNER, GAMES, FRIENDS</span>
        AND A MESSAGE
      </p>
    </section>

    <svg class="venue__pin" viewBox="0 0 24 32" aria-hidden="true">
      <path d="M12 0C5.4 0 0 5.3 0 11.8 0 20 12 32 12 32s12-12 12-20.2C24 5.3 18.6 0 12 0z" fill="#ffffff"/>
      <circle cx="12" cy="11.5" r="4.5" fill="#3a2a8a"/>
    </svg>
    <p class="venue">MERRIWICK'S – 4219 HOLLOWFERN<br>LN S, ASHBROOK, 97418</p>
  </article>
</body>
</html>
```